Catchy Cards for Hospital

I run a rural hospital in Texas called Pelham Ridge Hospital and am in need of contemporary business cards for all of my Department Heads. While our logo is somewhat simplistic, I don't have the option of changing it at this time, so anything to make the rest of the card present the appearance of a modern, professional healthcare facility would be great. Although the attached files are in black, our hospital colors are in a copper brown and black. I need to be able to change the name and title on the card so I can get cards printed for various department heads.

Target Market(s)

Referring physicians, large hospital systems, national organizations, state and federal government

Industry/Entity Type

Hospital

Contact Information for Business Card

Name Derek Solano
Title CEO

Phone: Main 541-740-2386 & Direct xxxxxx
Fax xxxxx
derek.solano@pelhamrh.com
382 Wilmot Street Box 415
Harlow Bend, Oregon 97412

Font styles to use
Serif

Colors
f48340

Requirements
Must have
• Clean crisp lines and ability to modify names, titles and emails
• On the back "PelhamRidgeHospital.Com
Nice to have
• Needs to be in line with logo, which is a bit dated and not too appealing, but I'm hoping that the rest of the card can make up for that fact just a little bit.
• Hospital's colors are a copper brown, black and white
Should not have
• Shapes or anything distracting

```html
<!DOCTYPE html>
<html lang="en">
<head>
<meta charset="utf-8">
<title>Pelham Ridge Hospital – Business Cards</title>
<link href="https://fonts.googleapis.com/css2?family=Arimo:wght@400;700&display=swap" rel="stylesheet">
<style>
  :root{
    --copper:#f48340;
    --copper-deep:#c8622a;
    --copper-band:#d9692c;
    --band-edge:#5a2c12;
    --ink:#1a1a1a;
    --paper:#ffffff;
    --paper-shade:#e4e4e4;
    --stage:#2b2b2b;
  }
  *{margin:0;padding:0;box-sizing:border-box}
  html,body{width:1200px;height:997px;overflow:hidden}
  body{background:var(--stage);font-family:"Arimo",Arial,sans-serif;position:relative}

  .card{position:absolute;width:560px;height:320px;border-radius:22px;overflow:hidden;
        box-shadow:0 14px 30px rgba(0,0,0,.55)}

  /* back of card */
  .card-back{left:110px;top:100px;background:linear-gradient(160deg,#f89150 0%,var(--copper) 45%,#e2733a 100%)}
  .card-back .brand-name{position:absolute;left:0;right:0;top:105px;text-align:center;
        color:var(--paper);font-weight:700;font-size:40px;letter-spacing:.5px}
  .card-back .web-band{position:absolute;left:0;right:0;top:238px;height:30px;background:var(--paper);
        border-top:2px solid var(--copper-deep);display:flex;align-items:center;justify-content:center;
        color:var(--ink);font-size:15px;letter-spacing:.5px}
  .card-back .tail-band{position:absolute;left:0;right:0;top:282px;height:16px;background:#efefef}

  /* front of card */
  .card-front{left:530px;top:520px;background:linear-gradient(180deg,var(--paper) 0%,#f4f4f4 60%,var(--paper-shade) 100%)}
  .card-front .brand-name{position:absolute;left:34px;top:108px;width:240px;color:var(--ink);
        font-weight:700;font-size:30px;line-height:1.1}
  .card-front .divider{position:absolute;left:300px;top:60px;width:2px;height:130px;
        background:linear-gradient(180deg,rgba(244,131,64,0),var(--copper) 40%,rgba(244,131,64,0))}
  .person{position:absolute;left:324px;top:68px}
  .person .name{color:var(--copper);font-weight:700;font-size:17px;letter-spacing:.5px}
  .person .title{color:var(--ink);font-weight:700;font-size:13px;margin-bottom:6px}
  .contact-list{list-style:none}
  .contact-list li{display:flex;align-items:center;gap:10px;font-size:14px;color:var(--ink);margin-top:5px;white-space:nowrap}
  .contact-list svg{width:13px;height:13px;flex:none}
  .address-band{position:absolute;left:0;right:0;top:218px;height:34px;background:var(--copper-band);
        border-top:2px solid var(--band-edge);border-bottom:2px solid var(--band-edge);display:flex;align-items:center;
        padding-left:44px;color:var(--ink);font-size:14px;font-weight:700;letter-spacing:.5px;white-space:nowrap}
  .foot-band{position:absolute;left:0;right:0;top:276px;height:22px;background:var(--copper)}
</style>
</head>
<body>

<section class="card card-back" aria-label="Card back">
  <div class="brand-name">Pelham Ridge Hospital</div>
  <div class="web-band">www.PelhamRidgeHospital.Com</div>
  <div class="tail-band"></div>
</section>

<section class="card card-front" aria-label="Card front">
  <div class="brand-name">Pelham Ridge Hospital</div>
  <div class="divider"></div>
  <div class="person">
    <div class="name">DEREK SOLANO</div>
    <div class="title">C.E.O</div>
    <ul class="contact-list">
      <li><svg viewBox="0 0 14 14"><circle cx="7" cy="7" r="7" fill="#f48340"/><path d="M4 5.5c1 2 2.5 3.5 4.5 4.5l1-1-1.2-.8-.6.5C6.8 8.2 5.8 7.2 5.3 6.3l.5-.6L5 4.5z" fill="#fff"/></svg>0800 55 4120</li>
      <li><svg viewBox="0 0 14 14"><circle cx="7" cy="7" r="7" fill="#f48340"/><rect x="4" y="5" width="6" height="4.5" rx="1" fill="#fff"/></svg>541-740-2386 &amp; XXXXXX</li>
      <li><svg viewBox="0 0 14 14"><circle cx="7" cy="7" r="7" fill="#f48340"/><rect x="3.8" y="4.8" width="6.4" height="4.4" fill="#fff"/><path d="M3.8 4.8L7 7.3l3.2-2.5" stroke="#f48340" stroke-width=".8" fill="none"/></svg>derek.solano@pelhamrh.com</li>
    </ul>
  </div>
  <div class="address-band">382 WILMOT STREET BOX 415 HARLOW BEND, OREGON 97412</div>
  <div class="foot-band"></div>
</section>

</body>
</html>
```